Tech Company Letterhead/Business Cards/Envelopes

We would like a new stationary design for a technology company that develops full turnkey solutions for governments related to Data, Identity Tracking, Fingerprinting, Passport Control, and Border Protection Systems.

We would like the stationary designs to include:

Letter Head
Business Cards
Envelopes

Target Market(s)

Corporate

Industry/Entity Type

Business

Contact Information for Business Card

Details to be shared with the winner.

Font styles to use
Serif
Sans Serif

Colors
e4daeb
85abd2
3176b5
0355a3
0692cd

```html
<!DOCTYPE html>
<html lang="en">
<head>
<meta charset="utf-8">
<title>Kalveren Stationery</title>
<link href="https://fonts.googleapis.com/css2?family=Open+Sans:wght@400;600;700&display=swap" rel="stylesheet">
<style>
:root{
  --backdrop:#8b5e3c;
  --paper:#ffffff;
  --brand-blue:#0b72b9;
  --brand-grey:#55565a;
  --ink:#55565a;
  --label:#ffffff;
}
*{margin:0;padding:0;box-sizing:border-box}
html,body{width:1200px;height:793px;overflow:hidden}
body{background:var(--backdrop);font-family:"Open Sans",sans-serif;color:var(--ink);position:relative}
.sheet{position:absolute;background:var(--paper);box-shadow:2px 3px 5px rgba(0,0,0,.35);overflow:hidden}
.wordmark{position:absolute;color:var(--brand-blue);font-weight:600;letter-spacing:.05em;line-height:1;white-space:nowrap}
.swoosh{position:absolute;left:0;bottom:0;width:100%;display:block}
.swoosh .band{fill:var(--brand-blue)}
.swoosh .stripe{fill:var(--brand-grey)}
.small{position:absolute;font-size:7.2px;line-height:1.7;white-space:nowrap}
.on-blue{color:#fff}
.key{color:var(--brand-blue)}
.web{font-weight:700;letter-spacing:.08em}
.option-label{position:absolute;color:var(--label);font-size:15px;width:253px;text-align:center}

.letterhead{left:62px;top:102px;width:488px;height:632px}
.letterhead .wordmark{left:0;width:100%;text-align:center;top:34px;font-size:38px}

.card{width:253px;height:144px}
.card-one{left:742px;top:54px}
.card-two{left:743px;top:238px;height:145px}
.card .wordmark{left:0;width:100%;text-align:center;top:19px;font-size:29px}
.divider{position:absolute;left:126px;top:72px;width:1px;height:34px;background:#ccc}

.envelope-flap{position:absolute;left:594px;top:422px;width:558px;height:64px}
.envelope-flap path{fill:var(--brand-blue)}
.envelope{left:590px;top:501px;width:560px;height:252px}
.envelope .wordmark{left:24px;top:22px;font-size:34px}
</style>
</head>
<body>

<div class="sheet letterhead">
  <div class="wordmark">KALVEREN</div>
  <svg class="swoosh" viewBox="0 0 600 100" preserveAspectRatio="none" style="height:88px">
    <path class="stripe" d="M0,0 C150,50 350,75 520,72 C340,82 150,68 0,24 Z"/>
    <path class="band" d="M0,24 C180,78 400,96 600,56 L600,100 L0,100 Z"/>
  </svg>
  <div class="small on-blue" style="left:20px;top:592px;line-height:1.65">P: 020 555 0142<br>E: info@kalveren.com<br>PO Box 01234, City Name, Country Name 00000</div>
  <div class="small on-blue web" style="right:20px;top:615px;font-size:8px">www.kalveren.com</div>
</div>

<div class="option-label" style="left:742px;top:30px">Option 1</div>
<div class="sheet card card-one">
  <div class="wordmark">KALVEREN</div>
  <div class="small" style="right:141px;top:72px;text-align:right"><span class="key">Phone</span> : 020 555 0142<br><span class="key">Email</span> : info@kalveren.com</div>
  <div class="divider"></div>
  <div class="small" style="right:16px;top:68px;text-align:right;line-height:1.6"><span class="key" style="letter-spacing:.05em">KALVEREN SYSTEMS</span><br>PO Box 01234, City Name<br>Country Name 00000</div>
  <svg class="swoosh" viewBox="0 0 600 100" preserveAspectRatio="none" style="height:48px">
    <path class="stripe" d="M0,0 C150,50 350,75 520,72 C340,82 150,68 0,24 Z"/>
    <path class="band" d="M0,24 C180,78 400,96 600,56 L600,100 L0,100 Z"/>
  </svg>
  <div class="small on-blue web" style="left:14px;top:123px;font-size:7.5px;letter-spacing:.03em">www.kalveren.com</div>
</div>

<div class="option-label" style="left:743px;top:213px">Option 2</div>
<div class="sheet card card-two">
  <div class="wordmark">KALVEREN</div>
  <svg class="swoosh" viewBox="0 0 600 100" preserveAspectRatio="none" style="height:93px">
    <path class="stripe" d="M0,0 C150,32 350,46 520,44 C340,50 150,42 0,14 Z"/>
    <path class="band" d="M0,14 C180,48 400,58 600,32 L600,100 L0,100 Z"/>
  </svg>
  <div class="small on-blue" style="left:15px;top:99px;line-height:1.6"><b style="font-weight:700">KALVEREN SYSTEMS</b><br><span style="display:inline-block;margin-top:3px">PO Box 01234, City Name</span><br>Country Name 00000</div>
  <div class="small on-blue" style="left:143px;top:98px;line-height:1.75">Phone : 020 555 0142<br>Email : info@kalveren.com<br><span class="web">www.kalveren.com</span></div>
</div>

<svg class="envelope-flap" viewBox="0 0 558 64" aria-hidden="true">
  <path d="M0,0 L558,0 L528,50 Q520,64 500,64 L58,64 Q38,64 30,50 Z"/>
</svg>
<div class="sheet envelope">
  <div class="wordmark">KALVEREN</div>
  <div class="small" style="left:24px;top:62px;line-height:1.6">PO Box 01234,&nbsp; City Name, Country Name 000 00<br><span class="key">Phone</span> : 020 555 0142 &nbsp;&nbsp; <span class="key">Email:</span> info@kalveren.com<br><span class="key web" style="margin-left:53px">www.kalveren.com</span></div>
  <svg class="swoosh" viewBox="0 0 600 100" preserveAspectRatio="none" style="height:81px">
    <path class="stripe" d="M0,0 C150,50 350,75 520,72 C340,82 150,68 0,24 Z"/>
    <path class="band" d="M0,24 C180,78 400,96 600,56 L600,100 L0,100 Z"/>
  </svg>
</div>

</body>
</html>
```